Tidewell Gin - Label for new Gin bottle

I am looking for a bottle label for our small batch, handcrafted Gin. We are located in the bay-side city of Saltmere (Victoria, Australia). I know I want more of a serious label but am torn between traditional or modern styling.

Label to include;
• Tidewell GIN (name)
• Hand Crafted
• Small Batch
• 40% Vol

Using 700ml MERIDA Spirit Bottle - Cork

Requirements
Must have
• Name; Tidewell Gin
Method: Hand Crafted
Batch Size; Small Batch
Alc; 40% Vol
Nice to have
• Maybe a coastal/seaside reference or reference to distilling.

```html
<!DOCTYPE html>
<html lang="en">
<head>
<meta charset="utf-8">
<title>Tidewell Gin – Label Concepts</title>
<link rel="stylesheet" href="https://fonts.googleapis.com/css2?family=Big+Shoulders+Display:wght@500&family=Montserrat:wght@600;700&family=Dosis:wght@500&display=swap">
<style>
  :root {
    --ink-blue: #1a3fd6;
    --label-blue: #0b3ae0;
    --silver: #d4d4cf;
    --muted: #9ea3b8;
    --paper: #ffffff;
  }
  * { margin: 0; padding: 0; box-sizing: border-box; }
  html, body { width: 1200px; height: 830px; overflow: hidden; background: var(--paper); }
  .canvas { position: relative; width: 1200px; height: 830px; }

  .neck-band { position: absolute; top: 155px; height: 44px; background: var(--label-blue); }
  .neck-band--huts { left: 260px; width: 238px; }
  .hut-strip {
    position: absolute; left: 2px; right: 2px; top: 6px; bottom: 4px;
    background: linear-gradient(90deg, #c9c3a8, #2a9ec9, #e0321c, #d6a31d, #8aa0b0, #c9c3a8, #2a9ec9, #e0321c, #d6a31d);
  }
  .neck-band--name {
    left: 702px; width: 239px;
    display: flex; align-items: center; justify-content: center;
    font-family: "Big Shoulders Display", sans-serif; font-weight: 500;
    font-size: 40px; letter-spacing: 1px; color: var(--silver); line-height: 1;
  }

  .label { position: absolute; text-align: center; }
  .label--clear { left: 255px; top: 372px; width: 240px; color: var(--ink-blue); }
  .label--diamond { left: 659px; top: 339px; width: 318px; height: 318px; color: var(--silver); }
  .diamond-shape { position: absolute; inset: 0; }
  .label__content { position: relative; display: flex; flex-direction: column; align-items: center; }

  .hut-row { background: var(--ink-blue); opacity: .85; }
  .label--clear .hut-row { width: 134px; height: 35px; }
  .label--diamond .label__content { padding-top: 80px; }
  .label--diamond .hut-row { width: 110px; height: 29px; background: #9fb0e8; opacity: .7; }

  .brand-name { font-family: "Big Shoulders Display", sans-serif; font-weight: 500; line-height: 1; letter-spacing: 1px; }
  .label--clear .brand-name { font-size: 46px; margin-top: 16px; }
  .label--diamond .brand-name { font-size: 38px; margin-top: 12px; }

  .tagline { font-family: "Montserrat", sans-serif; font-weight: 700; letter-spacing: 3px; }
  .label--clear .tagline--batch { font-size: 11px; margin-top: 12px; }
  .label--clear .tagline--lead { font-size: 12px; margin-top: 10px; }
  .label--clear .tagline--place { font-size: 7px; letter-spacing: 1.6px; margin-top: 9px; }
  .label--clear .tagline--country { font-size: 10px; margin-top: 7px; }
  .label--diamond .tagline--batch { font-size: 9px; margin-top: 9px; }
  .label--diamond .tagline--lead { font-size: 10px; margin-top: 8px; }
  .label--diamond .tagline--place { font-size: 5.8px; letter-spacing: 1.4px; margin-top: 7px; }
  .label--diamond .tagline--country { font-size: 8px; margin-top: 6px; }
  .strength { font-family: "Dosis", sans-serif; font-weight: 500; }
  .label--clear .strength { font-size: 11px; margin-top: 8px; }
  .label--diamond .strength { font-size: 9px; margin-top: 7px; color: var(--muted); }
</style>
</head>
<body>
<main class="canvas">

  <div class="neck-band neck-band--huts">
    <div class="hut-strip" role="img" aria-label="Row of colourful seaside bathing boxes"></div>
  </div>

  <section class="label label--clear">
    <div class="label__content">
      <div class="hut-row" role="img" aria-label="Line drawing of five bathing boxes"></div>
      <div class="brand-name">TIDEWELL GIN</div>
      <div class="tagline tagline--batch">SMALL BATCH</div>
      <div class="tagline tagline--lead">HAND CRAFTED</div>
      <div class="tagline tagline--place">SALTMERE VICTORIA</div>
      <div class="tagline tagline--country">AUSTRALIA</div>
      <div class="strength">40% VOL</div>
    </div>
  </section>

  <div class="neck-band neck-band--name">TIDEWELL GIN</div>

  <section class="label label--diamond">
    <svg class="diamond-shape" viewBox="0 0 318 318" aria-hidden="true">
      <polygon points="159,0 318,159 159,318 0,159" fill="var(--label-blue)"/>
    </svg>
    <div class="label__content">
      <div class="hut-row" role="img" aria-label="Line drawing of five bathing boxes"></div>
      <div class="brand-name">TIDEWELL GIN</div>
      <div class="tagline tagline--batch">SMALL BATCH</div>
      <div class="tagline tagline--lead">HAND CRAFTED</div>
      <div class="tagline tagline--place">SALTMERE VICTORIA</div>
      <div class="tagline tagline--country">AUSTRALIA</div>
      <div class="strength">40% VOL</div>
    </div>
  </section>

</main>
</body>
</html>
```